Letterbox flyer design

Hi - hoping you're able to help design a flyer for letterbox delivery. I think it needs to be 99mm x 210mm.

Side 1 - Large Logo, dark back ground.
Larger text - "5%* Property Management."
Medium Text - "Better Services, Lower Fee's, Higher Yields"
Smaller text at bottom - "0427 519 684 - marcus@kelbridge.com.au - kelbridge.com.au"

Back Side -
• Management Fee – 5%+GST of rent collected (no rent paid = no mgmt. fee charged)
• An Establishment fee of $500 for new tenancies we establish.
• Marketing Costs as Required and agreed to between parties.
• No Fee’s for Condition Reports, inspections, re-listing, tenancy renewal, admin costs, or any other ‘sundry’ charges.
• All rent is paid out monthly, yearly ‘profit-and-loss’ statements at no cost.
• Ingoing condition report is produced prior to occupancy, and routine condition inspections are conducted after the first 3months, then every 6months.
• Open homes are advertised in advance, and held on the weekend and one lunchtime or evening per week.
• All applicants are vetted, with the most suitable sent through for your consideration and approval.
• Advise on different tenancy terms as they could have the ability to affect the long-term yields.

```html
<!DOCTYPE html>
<html lang="en">
<head>
<meta charset="utf-8">
<title>Kelbridge &amp; Co – Letterbox Flyer</title>
<link rel="stylesheet" href="https://fonts.googleapis.com/css2?family=Anton&family=Lato:ital,wght@0,400;1,700&family=Poppins:wght@600;700&family=Roboto:wght@300;500&display=swap">
<style>
  :root {
    --backdrop: #c49a6c;
    --ink: #050608;
    --ink-soft: #111418;
    --teal: #3cc0c8;
    --teal-box: #37bdb4;
    --teal-deep: #14555a;
    --white: #ffffff;
    --grey: #8a8a8d;
    --grey-dark: #444446;
    --phone-teal: #16b3b3;
  }
  * { margin: 0; padding: 0; box-sizing: border-box; }
  html, body { width: 1200px; height: 1134px; overflow: hidden; background: var(--backdrop); }
  .canvas { position: relative; width: 1200px; height: 1134px; }

  /* ---------- Back side ---------- */
  .flyer-back {
    position: absolute; left: 170px; top: 161px; width: 403px; height: 854px;
    background: radial-gradient(ellipse at 70% 20%, var(--ink-soft), var(--ink) 70%);
    color: var(--white); font-family: "Roboto", sans-serif;
  }
  .fee-item { position: absolute; left: 43px; right: 8px; }
  .fee-item .tick { position: absolute; left: -16px; top: 5px; width: 14px; height: 12px; }
  .fee-title { font-family: "Poppins", sans-serif; font-weight: 600; color: var(--teal); font-size: 19.5px; line-height: 24px; letter-spacing: -0.1px; }
  .fee-detail { font-weight: 500; font-size: 14px; line-height: 18px; }
  .fee-note { font-weight: 300; font-size: 13px; line-height: 17px; }
  .fee-plain { font-weight: 500; font-size: 14px; line-height: 17px; }

  .frame-top { position: absolute; left: 0; top: 289px; width: 202px; height: 3px; background: var(--teal); }
  .frame-side { position: absolute; left: 2px; top: 289px; width: 3px; height: 333px; background: var(--teal); }
  .frame-bottom { position: absolute; left: 2px; top: 619px; width: 403px; height: 3px; background: var(--teal); }

  .no-fees { position: absolute; left: 20px; right: 10px; top: 306px; text-align: center; font-family: "Lato", sans-serif; font-size: 15.5px; line-height: 19px; }
  .service-box {
    position: absolute; left: 31px; top: 378px; width: 338px; height: 158px; border-radius: 12px;
    background: linear-gradient(180deg, #3ec3c0, var(--teal-box));
    color: var(--ink); font-family: "Lato", sans-serif; font-size: 12.4px; line-height: 15.5px; padding: 8px 10px 0 16px;
  }
  .service-box p { padding: 2px 0 6px; }
  .service-box hr { border: 0; border-top: 1px solid #10363a; margin: 0 18px 4px 0; }
  .vetting { position: absolute; left: 10px; right: 10px; top: 548px; text-align: center; font-family: "Lato", sans-serif; font-style: italic; font-weight: 700; font-size: 13.4px; line-height: 18px; }
  .web-pill {
    position: absolute; left: 92px; top: 604px; width: 221px; height: 35px; border-radius: 18px;
    background: var(--teal); color: var(--ink); font-family: "Roboto", sans-serif; font-weight: 500;
    font-size: 16px; letter-spacing: 0.8px; display: flex; align-items: center; justify-content: center;
  }

  .brand-ring { position: absolute; border: 3px solid var(--teal); border-radius: 50%; }
  .brand { position: absolute; left: 0; width: 403px; text-align: center; font-family: "Roboto", sans-serif; font-weight: 500; color: var(--grey); line-height: 1.2; }
  .flyer-back .brand-ring { left: 156px; top: 672px; width: 90px; height: 90px; }
  .flyer-back .brand { top: 772px; font-size: 15px; }
  .flyer-back .brand span { display: block; font-size: 13px; margin-top: 6px; }

  /* ---------- Front side ---------- */
  .flyer-front { position: absolute; left: 645px; top: 161px; width: 403px; height: 854px; background: var(--white); overflow: hidden; }
  .sky { position: absolute; left: 0; top: 0; width: 403px; height: 471px;
    background: radial-gradient(ellipse at 72% 22%, #a6dde2 0%, transparent 45%),
                linear-gradient(180deg, #4cc4d6 0%, #36c0c4 45%, #0bb9b5 70%, #1a8fa8 100%); }
  .sky-curve { position: absolute; left: 0; top: 420px; width: 403px; height: 52px; }
  .rate-disc { position: absolute; left: 66px; top: -61px; width: 260px; height: 260px; border-radius: 50%; background: var(--ink); border: 6px solid var(--teal-deep); }
  .rate { position: absolute; left: 122px; top: 39px; font-family: "Anton", sans-serif; color: var(--white); font-size: 122px; line-height: 1; letter-spacing: -1px; }
  .rate .pct { font-size: 104px; }
  .rate-star { position: absolute; left: 268px; top: 34px; font-family: "Roboto", sans-serif; font-weight: 500; color: var(--white); font-size: 22px; }
  .headline { position: absolute; left: 0; width: 403px; text-align: center; font-family: "Anton", sans-serif; color: var(--ink); line-height: 1; }
  .headline.line-1 { top: 216px; font-size: 64px; transform: scaleX(1.33); }
  .headline.line-2 { top: 279px; font-size: 47px; transform: scaleX(1.25); }
  .tagline { position: absolute; left: 0; width: 403px; top: 340px; text-align: center; font-family: "Poppins", sans-serif; font-weight: 700; color: var(--white); font-size: 22px; line-height: 31px; text-shadow: 0 1px 3px rgba(0,0,0,0.35); }
  .flyer-front .brand-ring { left: 119px; top: 462px; width: 166px; height: 166px; border-width: 4px; }
  .flyer-front .brand { top: 642px; font-size: 28px; }
  .flyer-front .brand span { display: block; font-size: 23px; margin-top: 14px; }
  .contact { position: absolute; left: 0; width: 403px; top: 760px; text-align: center; }
  .phone { display: inline-flex; align-items: center; gap: 6px; font-family: "Roboto", sans-serif; font-weight: 500; color: var(--phone-teal); font-size: 21px; }
  .phone svg { width: 21px; height: 21px; }
  .email { font-family: "Roboto", sans-serif; font-weight: 300; color: var(--grey-dark); font-size: 12.5px; letter-spacing: 0.6px; margin-top: 2px; }
  .contact-rule { width: 186px; height: 1px; background: var(--phone-teal); margin: 5px auto 3px; }
  .web { font-family: "Roboto", sans-serif; font-weight: 500; color: var(--grey-dark); font-size: 16.5px; letter-spacing: 0.4px; }
</style>
</head>
<body>
<main class="canvas">

  <section class="flyer-back">
    <div class="fee-item" style="top:41px">
      <svg class="tick" viewBox="0 0 14 12"><path d="M1 6 L5 10 L13 1" fill="none" stroke="var(--teal)" stroke-width="2"/></svg>
      <h2 class="fee-title">Management Fee</h2>
      <p class="fee-detail">5%+GST of rent collected</p>
      <p class="fee-note">(no rent paid = no mgmt. fee charged)</p>
    </div>
    <div class="fee-item" style="top:114px">
      <svg class="tick" viewBox="0 0 14 12"><path d="M1 6 L5 10 L13 1" fill="none" stroke="var(--teal)" stroke-width="2"/></svg>
      <h2 class="fee-title">An Establishment fee of $500</h2>
      <p class="fee-detail">for new tenancies we establish.</p>
    </div>
    <div class="fee-item" style="top:172px; right:0">
      <svg class="tick" viewBox="0 0 14 12"><path d="M1 6 L5 10 L13 1" fill="none" stroke="var(--teal)" stroke-width="2"/></svg>
      <h2 class="fee-title">All rent is paid out monthly, yearly</h2>
      <p class="fee-detail">‘profit-and-loss’ statements at no cost.</p>
    </div>
    <div class="fee-item" style="top:214px">
      <svg class="tick" viewBox="0 0 14 12" style="top:11px"><path d="M1 6 L5 10 L13 1" fill="none" stroke="var(--teal)" stroke-width="2"/></svg>
      <p class="fee-plain">Marketing Costs as Required and agreed to<br>between parties.</p>
    </div>

    <div class="frame-top"></div>
    <div class="frame-side"></div>
    <div class="frame-bottom"></div>

    <p class="no-fees">No Fee’s for Condition Reports, inspections,<br>re-listing, tenancy renewal, admin costs, or any<br>other ‘sundry’ charges.</p>

    <div class="service-box">
      <p>Ingoing condition report is produced prior to occupancy, and routine condition inspections are conducted after the first 3months, then every 6 months.</p>
      <hr>
      <p>Open homes are advertised in advance, and held on the weekend and one lunchtime or evening per week.</p>
      <hr>
      <p>Advise on different tenancy terms as they could have the ability to affect the long-term yields.</p>
    </div>

    <p class="vetting">All applicants are vetted, with the most suitable sent<br>through for your consideration and&nbsp; approval.</p>

    <div class="web-pill">www.kelbridge.com.au</div>

    <div class="brand-ring"></div>
    <p class="brand">KELBRIDGE &amp; CO<span>PROPERTY SERVICES</span></p>
  </section>

  <section class="flyer-front">
    <div class="sky" role="img" aria-label="Soft teal sky backdrop"></div>
    <svg class="sky-curve" viewBox="0 0 403 52" preserveAspectRatio="none">
      <path d="M0 52 L108 52 C140 10 170 0 201 0 C232 0 262 10 296 52 L403 52 Z" fill="var(--white)"/>
    </svg>

    <div class="rate-disc"></div>
    <p class="rate">5<span class="pct">%</span></p>
    <span class="rate-star">*</span>

    <h1 class="headline line-1">PROPERTY</h1>
    <p class="headline line-2">MANAGEMENT</p>
    <p class="tagline">Better Services, Lower<br>Fee's, Higher Yields</p>

    <div class="brand-ring"></div>
    <p class="brand">KELBRIDGE &amp; CO<span>PROPERTY SERVICES</span></p>

    <div class="contact">
      <div class="phone">
        <svg viewBox="0 0 24 24"><circle cx="12" cy="12" r="12" fill="var(--phone-teal)"/><path d="M8.2 5.5 L10 8.6 L8.8 10 C9.6 11.9 11.3 13.7 13.3 14.6 L14.6 13.4 L17.8 15.1 L17 17.8 C11.6 18 6.2 12.6 6.1 7 Z" fill="var(--ink)"/></svg>
        0427 519 684
      </div>
      <p class="email">marcus@kelbridge.com.au</p>
      <div class="contact-rule"></div>
      <p class="web">www.kelbridge.com.au</p>
    </div>
  </section>

</main>
</body>
</html>
```